Wanderlark Gin - Bottle Label for a craft Gin about to be launched on the world from New Zealand

We are a start up craft distillery in New Zealand. We have developed a wonderful Gin using our own grain spirit and both traditional and New Zealand native botanicals (Manuka to be specific), chosen our bottle and the name "Wanderlark" and done a bit of amateur label design and now we are looking for someone to make it great.

Feel free to change up our amateur concept but give us something that will pop from the back bar and scream authenticity, craft and individuality.

The attached files give you the specifications of the bottle, our current concept for a Wanderlark label and an earlier concept drawing that gives an idea of where we are thinking the two labels should go on the front of the bottle.

Thanks, we look forward to your ideas!!

Target Market(s)

High end and craft Gin drinkers. Hipsters and cocktail barflys and their bar tenders and bar owners

Requirements
Must have
• Attractive individuality
Nice to have
• Coolness
Should not have
• Uncoolness

```html
<!DOCTYPE html>
<html lang="en">
<head>
<meta charset="utf-8">
<title>Wanderlark Gin – Label Set</title>
<link href="https://fonts.googleapis.com/css2?family=Cinzel:wght@400;600&family=Playfair+Display:wght@500;600&family=Pinyon+Script&display=swap" rel="stylesheet">
<style>
  :root {
    --backdrop: #efe3c8;
    --label-black: #111111;
    --label-edge: #2a2a2a;
    --gold: #c9a45c;
    --gold-light: #e3c98f;
    --cream: #f3ead6;
    --white: #ffffff;
    --sketch-grey: #d9d9d9;
  }
  * { margin: 0; padding: 0; box-sizing: border-box; }
  html, body { width: 960px; height: 1200px; overflow: hidden; }
  body {
    background: var(--backdrop);
    display: flex;
    flex-direction: column;
    align-items: center;
    padding-top: 40px;
    gap: 28px;
    font-family: "Playfair Display", serif;
  }
  .neck-band {
    width: 200px;
    height: 84px;
    background: var(--label-black);
    border-radius: 6px;
    display: flex;
    align-items: center;
    justify-content: center;
  }
  .neck-band .brand-name {
    font-family: "Playfair Display", serif;
    font-weight: 600;
    font-size: 28px;
    color: var(--gold);
  }
  .front-label {
    width: 400px;
    height: 370px;
    background: var(--label-black);
    border: 2px solid var(--label-edge);
    border-radius: 10px;
    display: flex;
    flex-direction: column;
    align-items: center;
    padding-top: 58px;
    position: relative;
  }
  .front-label .brand-name {
    font-family: "Playfair Display", serif;
    font-weight: 600;
    font-size: 64px;
    line-height: 1;
    color: var(--cream);
  }
  .front-label .origin-line {
    margin-top: 20px;
    font-family: "Cinzel", serif;
    font-size: 15px;
    letter-spacing: 2px;
    color: var(--gold);
    display: flex;
    align-items: center;
    gap: 10px;
  }
  .origin-line .rule { width: 22px; height: 1px; background: var(--gold); }
  .front-label .crest {
    margin-top: 22px;
    width: 130px;
    height: 110px;
    border-radius: 6px;
    background: radial-gradient(circle at 50% 45%, var(--gold-light), var(--gold) 70%);
  }
  .front-label .volume {
    position: absolute;
    right: 24px;
    bottom: 20px;
    font-size: 15px;
    color: var(--white);
  }
  .botanical {
    width: 400px;
    height: 200px;
    border-radius: 10px;
    background: linear-gradient(160deg, var(--white), var(--sketch-grey));
  }
  .recipe-label {
    width: 400px;
    height: 330px;
    background: var(--label-black);
    border: 2px solid var(--label-edge);
    border-radius: 10px;
    display: flex;
    flex-direction: column;
    align-items: center;
    padding: 24px 30px 16px;
    color: var(--white);
  }
  .recipe-label .recipe-title {
    font-size: 28px;
    font-weight: 500;
  }
  .recipe-label .divider {
    width: 100%;
    margin-top: 14px;
    display: flex;
    align-items: center;
    justify-content: space-between;
  }
  .recipe-label .divider svg { display: block; }
  .recipe-label .tasting-note {
    margin-top: 12px;
    font-family: "Pinyon Script", cursive;
    font-size: 22px;
    line-height: 1.32;
    text-align: center;
  }
  .recipe-label .strength {
    margin-top: auto;
    width: 100%;
    display: flex;
    justify-content: space-between;
    font-size: 13px;
  }
</style>
</head>
<body>
  <div class="neck-band">
    <span class="brand-name">Wanderlark</span>
  </div>

  <section class="front-label">
    <h1 class="brand-name">Wanderlark</h1>
    <p class="origin-line"><span class="rule"></span>NEW ZEALAND SMALL BATCH<span class="rule"></span></p>
    <div class="crest" role="img" aria-label="Gold gin crest emblem with laurel sprays"></div>
    <span class="volume">500ml</span>
  </section>

  <div class="botanical" role="img" aria-label="Fine line engraving of a juniper sprig with berries"></div>

  <section class="recipe-label">
    <h2 class="recipe-title">Recipe#3</h2>
    <div class="divider">
      <svg width="340" height="8" viewBox="0 0 340 8" aria-hidden="true">
        <line x1="0" y1="4" x2="340" y2="4" stroke="#c9a45c" stroke-width="1"/>
        <circle cx="4" cy="4" r="2.5" fill="#c9a45c"/>
        <circle cx="336" cy="4" r="2.5" fill="#c9a45c"/>
      </svg>
    </div>
    <p class="tasting-note">
      A Classically Inspired Gin<br>
      With Developed Citrus<br>
      Notes From The Manuka<br>
      Berries From Rowan's<br>
      Mates. Best With An Equal<br>
      Mix Of Some Fancy Tonic
    </p>
    <div class="strength">
      <span>84 proof</span>
      <span>42% Alc by Vol</span>
    </div>
  </section>
</body>
</html>
```